Postcard Design Project( QPRX 6.5in wide x 9in )

Painting Company
- Interior and Exterior Painting
- Wallpaper Removal and Installation
- Wood Staining
-Licensed and Insured HIC #KT739208
-website: www.kellermontpainting.com
-Facebook: @kmpainting
-Phone #: 555-318-2076
Fall Special Discount 10% off $500.00 or more
(QPRX Postcard size (6.5in wide x9)

People who are in need of painting

Painting

• Must be bold and make a statement. I need the people to hold on to the postcard and not throw it away.
• Should not look like you took it off a template.

```html
<!DOCTYPE html>
<html lang="en">
<head>
<meta charset="utf-8">
<title>Kellermont Painting — Fall Postcard</title>
<link href="https://fonts.googleapis.com/css2?family=Source+Sans+3:wght@400;600;700;800&display=swap" rel="stylesheet">
<style>
  :root{
    --navy:#2e2f6e;
    --red:#c1202f;
    --gold:#f2b51c;
    --gray:#d9d9dc;
    --white:#ffffff;
    --ink:#3a3a3a;
    --page:#ececec;
  }
  *{margin:0;padding:0;box-sizing:border-box}
  html,body{width:1200px;height:960px;overflow:hidden;background:var(--page);
    font-family:"Source Sans 3",Arial,sans-serif}
  .postcard{position:absolute;left:305px;width:590px;height:426px;background:var(--white);
    overflow:hidden;box-shadow:0 6px 18px rgba(0,0,0,.18)}
  .postcard--front{top:34px}
  .postcard--back{top:500px}
  .shapes{position:absolute;inset:0}

  .brand{position:absolute;display:flex;align-items:center;gap:10px;color:var(--navy);
    font-weight:800;text-transform:uppercase;line-height:.95}
  .brand__mark{width:14px;height:14px;background:var(--red);flex:none}
  .front .brand{left:26px;top:36px;font-size:32px}
  .back .brand{left:28px;top:20px;font-size:17px;gap:8px}
  .back .brand__mark{width:11px;height:11px}

  .services-tag{position:absolute;left:0;top:206px;width:152px;height:32px;background:var(--red);
    border-radius:0 16px 16px 0;color:var(--white);font-weight:600;font-size:19px;letter-spacing:.5px;
    padding:4px 0 0 20px}
  .services-list{position:absolute;left:20px;top:250px;list-style:none;color:var(--white);font-size:15px;line-height:25px}
  .services-list li{display:flex;align-items:center;gap:7px}
  .services-list li::before{content:"";width:7px;height:7px;border:1.5px solid var(--red);border-radius:50%}

  .discount{position:absolute;border:1.5px solid var(--gold);color:var(--white);text-align:center;text-transform:uppercase}
  .discount__label{font-weight:600}
  .discount__value{color:var(--gold);font-weight:800;line-height:1}
  .front .discount{left:20px;top:334px;width:254px;height:74px;padding-top:7px}
  .front .discount__label{font-size:12px}
  .front .discount__value{font-size:28px}
  .front .discount__min{font-size:11px}
  .back .discount{left:70px;top:246px;width:230px;height:56px;padding-top:4px}
  .back .discount__label{font-size:10px}
  .back .discount__value{font-size:21px}
  .back .discount__min{font-size:9px}

  .license{position:absolute;font-size:10px}
  .front .license{right:14px;top:370px;color:var(--white)}
  .back .license{left:0;width:370px;text-align:center;top:344px;color:var(--ink);font-size:9.5px}

  .call{position:absolute;background:var(--red);color:var(--white);display:flex;align-items:center;
    justify-content:center;gap:12px;font-weight:600;text-transform:uppercase}
  .call__phone{display:flex;align-items:center;gap:6px;font-weight:700}
  .front .call{right:0;top:388px;width:298px;height:30px;border-radius:15px 0 0 15px;font-size:16px}
  .back .call{left:40px;top:312px;width:290px;height:26px;border-radius:13px;font-size:14px}

  .back .about{position:absolute;left:24px;top:64px;width:310px;color:var(--red);font-size:10.5px;line-height:13px;text-align:center}
  .back .website{position:absolute;left:0;width:370px;text-align:center;top:358px;color:var(--red);font-weight:700;font-size:15px}
  .back .social{position:absolute;left:0;width:370px;top:380px;display:flex;justify-content:center;align-items:center;gap:6px;color:var(--ink);font-size:12px}
  .social__mark{width:10px;height:10px;background:var(--navy)}
  .postal{position:absolute;left:440px;top:40px;width:120px;height:44px;border:1px dashed #888;
    font-size:10px;color:var(--ink);padding:6px 8px;line-height:13px}
</style>
</head>
<body>

<section class="postcard postcard--front front" aria-label="Postcard front">
  <svg class="shapes" viewBox="0 0 590 426">
    <defs>
      <linearGradient id="house" x1="0" y1="0" x2="1" y2="1">
        <stop offset="0" stop-color="#a8432e"/>
        <stop offset=".3" stop-color="#6f8a4c"/>
        <stop offset=".6" stop-color="#7b889e"/>
        <stop offset="1" stop-color="#9c9386"/>
      </linearGradient>
      <radialGradient id="leaf" cx=".4" cy=".4" r=".6">
        <stop offset="0" stop-color="#ffd24a"/>
        <stop offset=".7" stop-color="#f0901c"/>
        <stop offset="1" stop-color="#d0531a"/>
      </radialGradient>
      <radialGradient id="wallpaper" cx=".4" cy=".4" r=".7"><stop offset="0" stop-color="#f5efe2"/><stop offset="1" stop-color="#cdbf9f"/></radialGradient>
      <radialGradient id="wood" cx=".4" cy=".4" r=".7"><stop offset="0" stop-color="#d29a62"/><stop offset="1" stop-color="#8a4e22"/></radialGradient>
      <radialGradient id="roller" cx=".4" cy=".4" r=".7"><stop offset="0" stop-color="#e2f0f6"/><stop offset="1" stop-color="#9cc6da"/></radialGradient>
    </defs>
    <path d="M292,0 L590,0 L590,292 C480,302 400,300 340,262 C296,226 276,170 278,100 C280,50 284,18 292,0 Z" fill="url(#house)" role="img" aria-label="Photo of a blue house with autumn trees and a leaf-covered driveway"/>
    <path d="M0,176 C120,166 220,188 300,240 C380,292 480,302 590,282 L590,298 C480,318 380,308 300,256 C220,204 120,182 0,192 Z" fill="var(--gray)"/>
    <path d="M0,184 C120,174 220,196 300,248 C380,300 480,310 590,290 L590,300 C480,320 380,310 300,258 C220,206 120,190 0,196 Z" fill="var(--red)"/>
    <path d="M0,194 C120,186 220,208 300,260 C380,312 480,320 590,300 L590,426 L0,426 Z" fill="var(--navy)"/>
    <circle cx="330" cy="288" r="44" fill="url(#wallpaper)" stroke="var(--white)" stroke-width="4" role="img" aria-label="Photo of wallpaper being removed"/>
    <circle cx="430" cy="322" r="44" fill="url(#wood)" stroke="var(--white)" stroke-width="4" role="img" aria-label="Photo of wood staining with a brush"/>
    <circle cx="530" cy="290" r="44" fill="url(#roller)" stroke="var(--white)" stroke-width="4" role="img" aria-label="Photo of a wall being painted with a roller"/>
    <g fill="url(#leaf)">
      <circle cx="44" cy="158" r="20" role="img" aria-label="Autumn maple leaves"/>
      <circle cx="76" cy="172" r="10"/>
      <circle cx="300" cy="240" r="15" role="img" aria-label="Autumn maple leaf"/>
      <circle cx="560" cy="254" r="17" role="img" aria-label="Autumn maple leaves"/>
      <circle cx="536" cy="248" r="10"/>
      <circle cx="44" cy="371" r="15" role="img" aria-label="Autumn maple leaf"/>
      <circle cx="252" cy="370" r="15" role="img" aria-label="Autumn maple leaf"/>
    </g>
  </svg>

  <div class="brand"><span class="brand__mark"></span><span class="brand__name">Kellermont<br>Painting</span></div>

  <div class="services-tag">SERVICES</div>
  <ul class="services-list">
    <li>Interior and Exterior Painting</li>
    <li>Wallpaper Removal and Installation</li>
    <li>Wood Staining</li>
  </ul>

  <div class="discount">
    <div class="discount__label">Fall Special Discount</div>
    <div class="discount__value">10% Off</div>
    <div class="discount__min">$500.00 or more</div>
  </div>

  <div class="license">Licensed and Insured HIC #KT739208</div>
  <div class="call">Call us now!
    <span class="call__phone">
      <svg width="14" height="14" viewBox="0 0 24 24"><path d="M6.6 10.8a15 15 0 0 0 6.6 6.6l2.2-2.2a1 1 0 0 1 1-.25 11 11 0 0 0 3.6.6 1 1 0 0 1 1 1V20a1 1 0 0 1-1 1A17 17 0 0 1 3 4a1 1 0 0 1 1-1h3.5a1 1 0 0 1 1 1 11 11 0 0 0 .6 3.6 1 1 0 0 1-.25 1z" fill="none" stroke="#fff" stroke-width="2"/></svg>
      555-318-2076</span>
  </div>
</section>

<section class="postcard postcard--back back" aria-label="Postcard back">
  <svg class="shapes" viewBox="0 0 590 426">
    <defs>
      <radialGradient id="leafB" cx=".4" cy=".4" r=".6">
        <stop offset="0" stop-color="#ffd24a"/>
        <stop offset=".7" stop-color="#f0901c"/>
        <stop offset="1" stop-color="#d0531a"/>
      </radialGradient>
      <radialGradient id="hall" cx=".4" cy=".4" r=".7"><stop offset="0" stop-color="#efe4d0"/><stop offset="1" stop-color="#8a5a32"/></radialGradient>
      <radialGradient id="stairs" cx=".4" cy=".4" r=".7"><stop offset="0" stop-color="#ecebe8"/><stop offset="1" stop-color="#8c8883"/></radialGradient>
      <radialGradient id="kitchen" cx=".4" cy=".4" r=".7"><stop offset="0" stop-color="#f6efe4"/><stop offset="1" stop-color="#a98a62"/></radialGradient>
    </defs>
    <path d="M0,130 C200,118 330,120 380,150 C410,190 420,260 400,330 L0,330 Z" fill="var(--navy)"/>
    <path d="M0,336 L398,336 C392,370 384,400 372,426 L0,426 Z" fill="#eeeef0"/>
    <circle cx="80" cy="200" r="42" fill="url(#hall)" stroke="var(--white)" stroke-width="4" role="img" aria-label="Photo of an entry hall with a wooden door"/>
    <circle cx="180" cy="186" r="40" fill="url(#stairs)" stroke="var(--white)" stroke-width="4" role="img" aria-label="Photo of a staircase interior"/>
    <circle cx="280" cy="168" r="40" fill="url(#kitchen)" stroke="var(--white)" stroke-width="4" role="img" aria-label="Photo of a painted kitchen interior"/>
    <g fill="url(#leafB)">
      <circle cx="92" cy="282" r="11" role="img" aria-label="Autumn maple leaf"/>
      <circle cx="280" cy="260" r="12" role="img" aria-label="Autumn maple leaf"/>
    </g>
  </svg>

  <div class="brand"><span class="brand__mark"></span><span class="brand__name">Kellermont Painting</span></div>
  <p class="about">Kellermont Painting is a Veteran-owned business with experience of providing quality work for 10+ years in residential homes.</p>

  <div class="discount">
    <div class="discount__label">Fall Special Discount</div>
    <div class="discount__value">10% Off</div>
    <div class="discount__min">$500.00 or more</div>
  </div>

  <div class="call">Call us now!
    <span class="call__phone">
      <svg width="12" height="12" viewBox="0 0 24 24"><path d="M6.6 10.8a15 15 0 0 0 6.6 6.6l2.2-2.2a1 1 0 0 1 1-.25 11 11 0 0 0 3.6.6 1 1 0 0 1 1 1V20a1 1 0 0 1-1 1A17 17 0 0 1 3 4a1 1 0 0 1 1-1h3.5a1 1 0 0 1 1 1 11 11 0 0 0 .6 3.6 1 1 0 0 1-.25 1z" fill="none" stroke="#fff" stroke-width="2"/></svg>
      555-318-2076</span>
  </div>
  <div class="license">Licensed and Insured HIC #KT739208</div>
  <div class="website">www.kellermontpainting.com</div>
  <div class="social"><span class="social__mark"></span>@kmpainting</div>

  <div class="postal">Local<br>Postal Customer</div>
</section>

</body>
</html>
```